Book cover for a book about time management for women

We need a book cover for a book about time management for women written by a woman. Even though the book has a provocative title "Calendar candy" based on the seminars the author holds for women seeking the change in their life, it has nothing to do with the words themselves. The subtitle is "Keep each morning in your grip. A bold guide on daily rhythm for ladies today"

Preferred fonts (not necessarily):
Plus Jakarta Sans
Tiempos Headline

Preferred colours (not necessarily):
- orange
- pastel "highlighters"

We look for a simple/clean design that catches the attention of the women without too many graphic elements.

Target Market(s)

Women that want to change and organise their life

Industry/Entity Type

productivity, marketing, work-life balance

Font styles to use
Other font styles liked:
• Plus Jakarta Sans, Tiempos Headline

Colors
F0912C
F2A743
F7CA91
FBE8D2
FDF5EE
A7469A
B969AE
D3A5CF
EDDBEB
F8F0F9

Requirements
Must have
• Famine feeling as the target audience are women with drive to better life
Should not have
• No explicit images or sexually motivated themes

```html
<!DOCTYPE html>
<html lang="en">
<head>
<meta charset="utf-8">
<title>Calendar Candy — Book Cover</title>
<link href="https://fonts.googleapis.com/css2?family=Plus+Jakarta+Sans:wght@400;500;700&family=Source+Serif+4:opsz,wght@8..60,500;8..60,600&display=swap" rel="stylesheet">
<style>
  :root {
    --backdrop: #000000;
    --paper: #ffffff;
    --plum: #a7469a;
    --orchid: #b969ae;
    --lilac: #d3a5cf;
    --lilac-pale: #eddbeb;
    --lilac-mist: #f8f0f9;
    --orange: #f0912c;
    --orange-soft: #f2a743;
    --peach: #f7ca91;
  }
  * { margin: 0; padding: 0; box-sizing: border-box; }
  html, body {
    width: 1200px;
    height: 1200px;
    overflow: hidden;
    background: var(--backdrop);
  }
  .canvas {
    position: relative;
    width: 1200px;
    height: 1200px;
  }
  .cover {
    position: absolute;
    left: 360px;
    top: 240px;
    width: 480px;
    height: 720px;
    background: var(--paper);
    overflow: hidden;
  }
  .title {
    position: absolute;
    top: 30px;
    left: 0;
    width: 100%;
    text-align: center;
    font-family: "Source Serif 4", Georgia, serif;
    color: var(--plum);
    line-height: 1;
  }
  .title-kicker {
    display: block;
    font-size: 50px;
    font-weight: 500;
    letter-spacing: 1px;
  }
  .title-main {
    display: block;
    margin-top: 2px;
    font-size: 132px;
    font-weight: 500;
    letter-spacing: -1px;
  }
  .artwork {
    position: absolute;
    left: 66px;
    top: 206px;
    width: 346px;
    height: 240px;
    border-radius: 46% 54% 38% 48% / 52% 44% 46% 40%;
    background:
      radial-gradient(ellipse 22% 34% at 50% 62%, var(--orange-soft) 0%, var(--peach) 55%, rgba(247, 202, 145, 0) 100%),
      radial-gradient(ellipse 30% 45% at 50% 45%, var(--orchid) 0%, rgba(185, 105, 174, 0) 100%),
      radial-gradient(ellipse at 50% 55%, var(--lilac) 0%, var(--lilac-pale) 55%, var(--lilac-mist) 100%);
  }
  .tagline {
    position: absolute;
    top: 460px;
    left: 0;
    width: 100%;
    text-align: center;
    font-family: "Plus Jakarta Sans", Arial, sans-serif;
    font-weight: 700;
    font-size: 37px;
    line-height: 47px;
    letter-spacing: 1px;
    color: var(--plum);
    text-transform: uppercase;
  }
  .promise-band {
    position: absolute;
    top: 564px;
    left: 0;
    width: 100%;
    height: 82px;
    background: var(--orange);
    display: flex;
    align-items: center;
    justify-content: center;
    text-align: center;
    font-family: "Plus Jakarta Sans", Arial, sans-serif;
    font-weight: 400;
    font-size: 21px;
    line-height: 27px;
    letter-spacing: 0.5px;
    color: var(--paper);
    text-transform: uppercase;
  }
  .author-band {
    position: absolute;
    top: 646px;
    left: 0;
    width: 100%;
    height: 74px;
    background: var(--plum);
    border-top: 4px solid var(--orchid);
    display: flex;
    align-items: center;
    justify-content: center;
    font-family: "Plus Jakarta Sans", Arial, sans-serif;
    font-weight: 500;
    font-size: 24px;
    letter-spacing: 2px;
    color: var(--paper);
    text-transform: uppercase;
  }
</style>
</head>
<body>
  <main class="canvas">
    <section class="cover">
      <h1 class="title">
        <span class="title-kicker">CALENDAR</span>
        <span class="title-main">CANDY</span>
      </h1>
      <div class="artwork" role="img" aria-label="Illustration of a woman in an orange top sitting cross-legged in calm meditation, surrounded by floating office items: clipboard, phone, laptop, coffee cup, envelope, calculator and calendar"></div>
      <p class="tagline">Keep each morning<br>in your grip</p>
      <p class="promise-band">A bold guide on daily rhythm<br>for ladies today</p>
      <p class="author-band">Author Names</p>
    </section>
  </main>
</body>
</html>
```